Design for web app with Brindle Surface System - Tarvo7 SMS consult

We are developing a web app that will work in browsers. Its main purpose is to allow for users (signing up and logging in with their phone number) to track their habbits and select consultants to whom they can send SMS for help.

The wireframes of the app can be accessed here (pdf):
https://files.quellbox.example/d/7Kx2PmR9vTq4LnZ8wYs3HbJ6cFe1/view?usp=sharing

NB!: Please do not follow the mockups 100% literally, but the Brindle Surface system guidelines.

The technical specifications and descriptions of the web app's functionalities are available in the link below:
https://pages.quellbox.example/document/d/4TrNk8WqZp2LmVx7YcBs9HdJ3fRe6GaU1oKi5QeXtwy0/edit?usp=sharing

Requirements for the design:

- The design should be provided as PSD, where each page/section should be in its own PSD file OR all pages/sections should be represented as folder groups in a single PSD file.

- All graphical elements in the design should be delivered as single layers which can then be extracted from the PSD.

- All graphical elements (icons, graphical buttons, etc.) should be provided as vector objects in the PSD, so that they can be exported into different sizes without loss of quality (for responsiveness).

- The design should use either web safe fonts or Brindle Type.

Instructions for the design:
The design should be based on Brindle Surface System - http://www.brindle.example/design/spec/surface-system/introduction.html

Please also provide an app icon and suggest a logo for the app.

• Based on Brindle Surface System
• Flat
• Nice looking and not so stiff as the default Brindle Surface System, but it is important to follow their guidelines.
• 3D

```html
<!DOCTYPE html>
<html lang="en">
<head>
<meta charset="utf-8">
<title>Tarvo7 SMS consult – app screens</title>
<link rel="stylesheet" href="https://fonts.googleapis.com/css2?family=Roboto:wght@400;500;700&display=swap">
<style>
  :root{
    --page:#ebebeb;
    --blue:#1690d8;
    --blue-dark:#0c70ad;
    --green:#67d56f;
    --green-deep:#4cc457;
    --red:#ef5b3b;
    --surface:#f7f8f8;
    --white:#ffffff;
    --line:#e6e8ea;
    --text:#3d4247;
    --muted:#9aa1a6;
    --btn-grey:#eef0f2;
    --avatar:#b9a99a;
  }
  *{box-sizing:border-box;margin:0;padding:0}
  html,body{width:1200px;height:1000px;overflow:hidden}
  body{background:var(--page);font-family:'Roboto',Arial,sans-serif;color:var(--text);position:relative}

  .screen{position:absolute;width:225px;height:400px;background:var(--surface);overflow:hidden}
  .abs{position:absolute}

  .status{position:absolute;left:0;top:0;width:100%;height:14px;background:var(--blue-dark);
    display:flex;justify-content:flex-end;align-items:center;gap:4px;padding-right:6px;
    color:var(--white);font-size:8px}
  .status svg{display:block}
  .appbar{position:absolute;left:0;top:14px;width:100%;height:36px;background:var(--blue);
    color:var(--white);font-size:12px;font-weight:500;display:flex;align-items:center;justify-content:center}
  .appbar .back{position:absolute;left:10px;top:12px}

  .field{position:absolute;left:12px;width:200px;height:33px;background:var(--white);
    border:1px solid var(--line);border-radius:2px;font-size:9px;color:var(--muted);
    padding:0 10px;display:flex;align-items:center}
  .btn{position:absolute;left:12px;width:200px;height:34px;border-radius:2px;font-size:8px;font-weight:500;
    letter-spacing:.4px;text-transform:uppercase;display:flex;align-items:center;justify-content:center;gap:6px;
    box-shadow:0 1px 1px rgba(0,0,0,.12)}
  .btn-blue{background:var(--blue);color:var(--white);border:1px solid var(--blue-dark)}
  .btn-green{background:var(--green);color:var(--white);border:1px solid var(--green-deep)}
  .btn-grey{background:var(--btn-grey);color:var(--text);border:1px solid #dadde0}

  .wordmark{position:absolute;left:0;width:100%;text-align:center;font-weight:700;letter-spacing:1px}

  .splash{background:linear-gradient(200deg,#17a0d4 0%,#2db3b0 45%,#5fd07a 100%)}

  .row{position:absolute;left:0;width:100%;height:48px;border-bottom:1px solid var(--line);
    background:var(--white);display:flex;align-items:center;padding:0 12px}
  .avatar{width:32px;height:32px;border-radius:50%;background:radial-gradient(circle at 50% 40%,#d8c4b3,#8a7c70);flex:none}
  .row .name{margin-left:10px;font-size:10px;flex:1}
  .tick{width:16px;height:16px;border-radius:50%;background:var(--green);display:flex;align-items:center;justify-content:center}
  .plus{width:14px;height:14px;border-radius:50%;background:#eceef0;display:flex;align-items:center;justify-content:center}

  .caption{position:absolute;left:0;width:100%;text-align:center;font-size:9.5px;color:var(--text);line-height:12px}

  .dropband{position:absolute;left:0;top:50px;width:100%;height:38px;background:var(--blue)}
  .dropdown{position:absolute;left:12px;top:50px;width:200px;height:30px;background:var(--white);border-radius:2px;
    font-size:9.5px;padding:0 10px;display:flex;align-items:center;justify-content:space-between;
    box-shadow:0 1px 2px rgba(0,0,0,.15)}

  .card{position:absolute;left:12px;top:100px;width:200px;background:var(--white);box-shadow:0 1px 2px rgba(0,0,0,.14)}
  .card-head{height:33px;background:var(--green);color:var(--white);font-size:10px;font-weight:500;
    display:flex;align-items:center;justify-content:space-around}
  .day{height:41.5px;border-bottom:1px solid var(--line);display:flex;align-items:center;justify-content:space-between;
    padding:0 12px;font-size:9.5px}
  .dot{width:7px;height:7px;border-radius:50%}
  .dot.ok{background:var(--green)}
  .dot.bad{background:var(--red)}

  .calendar{display:grid;grid-template-columns:repeat(7,1fr)}
  .calendar .wd{height:22px;font-size:6px;color:var(--muted);display:flex;align-items:center;justify-content:center;
    border-right:1px solid var(--line);border-bottom:1px solid var(--line)}
  .calendar .cell{height:28.5px;font-size:9.5px;display:flex;align-items:center;justify-content:center;
    border-right:1px solid var(--line);border-bottom:1px solid var(--line)}
  .calendar .cell span{width:19px;height:19px;border-radius:50%;display:flex;align-items:center;justify-content:center}
  .calendar .g span{background:var(--green);color:var(--white)}
  .calendar .r span{background:var(--red);color:var(--white)}

  .textarea{position:absolute;left:12px;width:200px;background:var(--white);border:1px solid var(--line);
    border-radius:2px;font-size:8.5px;color:var(--muted);padding:10px}
</style>
</head>
<body>

<!-- Row 1 -->
<section class="screen splash" style="left:20px;top:90px">
  <div class="status"><svg width="7" height="7"><path d="M7 0V7H0Z" fill="#fff" opacity=".8"/></svg><svg width="5" height="7"><rect x="0.5" y="0.5" width="4" height="6" fill="#fff"/></svg>02:40</div>
  <div class="wordmark" style="top:180px;font-size:34px;color:var(--white)">Tarvo7</div>
</section>

<section class="screen" style="left:254px;top:90px">
  <div class="status"><svg width="7" height="7"><path d="M7 0V7H0Z" fill="#fff" opacity=".8"/></svg><svg width="5" height="7"><rect x="0.5" y="0.5" width="4" height="6" fill="#fff"/></svg>02:40</div>
  <header class="appbar">Login</header>
  <div class="wordmark" style="top:100px;font-size:32px;color:var(--blue)">Tarvo7</div>
  <div class="field" style="top:192px">Phone</div>
  <div class="field" style="top:234px">Password</div>
  <div class="btn btn-blue" style="top:275px">Login</div>
  <div class="caption" style="top:319px;font-size:8px">Forgot your password?</div>
  <div class="btn btn-green" style="top:354px">Signup</div>
</section>

<section class="screen" style="left:488px;top:90px">
  <div class="status"><svg width="7" height="7"><path d="M7 0V7H0Z" fill="#fff" opacity=".8"/></svg><svg width="5" height="7"><rect x="0.5" y="0.5" width="4" height="6" fill="#fff"/></svg>02:40</div>
  <header class="appbar">Signup</header>
  <div class="wordmark" style="top:132px;font-size:32px;color:var(--blue)">Tarvo7</div>
  <div class="field" style="top:255px">Phone</div>
  <div class="btn btn-green" style="top:295px">Signup</div>
  <div class="btn btn-grey" style="top:355px"><svg width="7" height="7"><path d="M1 1L6 6M6 1L1 6" stroke="#3d4247" stroke-width="1.2"/></svg>Cancel</div>
</section>

<section class="screen" style="left:721px;top:90px">
  <div class="status"><svg width="7" height="7"><path d="M7 0V7H0Z" fill="#fff" opacity=".8"/></svg><svg width="5" height="7"><rect x="0.5" y="0.5" width="4" height="6" fill="#fff"/></svg>02:40</div>
  <header class="appbar">Select Your Consultants</header>
  <div class="row" style="top:50px"><div class="avatar" role="img" aria-label="Portrait of consultant Oren Vasko"></div><span class="name">Oren Vasko</span><span class="tick"><svg width="8" height="8"><path d="M1 4L3.2 6.2L7 2" stroke="#fff" stroke-width="1.3" fill="none"/></svg></span></div>
  <div class="row" style="top:98px"><div class="avatar" role="img" aria-label="Portrait of consultant Milo Harrow"></div><span class="name">Milo Harrow</span><span class="plus"><svg width="7" height="7"><path d="M3.5 0.5V6.5M0.5 3.5H6.5" stroke="#9aa1a6" stroke-width="1"/></svg></span></div>
  <div class="row" style="top:146px"><div class="avatar" role="img" aria-label="Portrait of consultant Dane Colby"></div><span class="name">Dane Colby</span><span class="plus"><svg width="7" height="7"><path d="M3.5 0.5V6.5M0.5 3.5H6.5" stroke="#9aa1a6" stroke-width="1"/></svg></span></div>
  <div class="row" style="top:194px"><div class="avatar" role="img" aria-label="Portrait of consultant Ivo Brandt"></div><span class="name">Ivo Brandt</span><span class="tick"><svg width="8" height="8"><path d="M1 4L3.2 6.2L7 2" stroke="#fff" stroke-width="1.3" fill="none"/></svg></span></div>
  <div class="row" style="top:242px"><div class="avatar" role="img" aria-label="Portrait of consultant Teo Marsh"></div><span class="name">Teo Marsh</span><span class="tick"><svg width="8" height="8"><path d="M1 4L3.2 6.2L7 2" stroke="#fff" stroke-width="1.3" fill="none"/></svg></span></div>
  <div class="row" style="top:290px"><div class="avatar" role="img" aria-label="Portrait of consultant Gil Ashford"></div><span class="name">Gil Ashford</span><span class="tick"><svg width="8" height="8"><path d="M1 4L3.2 6.2L7 2" stroke="#fff" stroke-width="1.3" fill="none"/></svg></span></div>
  <div class="btn btn-blue" style="top:354px">Continue</div>
</section>

<section class="screen" style="left:955px;top:90px">
  <div class="status"><svg width="7" height="7"><path d="M7 0V7H0Z" fill="#fff" opacity=".8"/></svg><svg width="5" height="7"><rect x="0.5" y="0.5" width="4" height="6" fill="#fff"/></svg>02:40</div>
  <header class="appbar">Contact Your Consultant</header>
  <div class="abs" style="left:0;top:50px;width:225px;height:90px;background:var(--white);border-bottom:1px solid var(--line)"></div>
  <svg class="abs" style="left:12px;top:62px" width="6" height="8"><path d="M5 1L2 4L5 7" stroke="#555" fill="none"/></svg>
  <div class="caption" style="top:60px;font-size:9.5px">16 June 2015</div>
  <svg class="abs" style="left:207px;top:62px" width="6" height="8"><path d="M1 1L4 4L1 7" stroke="#555" fill="none"/></svg>
  <div class="btn btn-green" style="top:86px;left:33px;width:159px"><svg width="9" height="9" viewBox="0 0 24 24"><path d="M6.6 10.8c1.4 2.8 3.8 5.1 6.6 6.6l2.2-2.2c.3-.3.7-.4 1-.2 1.1.4 2.3.6 3.6.6.6 0 1 .4 1 1V20c0 .6-.4 1-1 1C10.6 21 3 13.4 3 4c0-.6.4-1 1-1h3.5c.6 0 1 .4 1 1 0 1.3.2 2.5.6 3.6.1.3 0 .7-.2 1z" fill="#fff"/></svg>Call me</div>
  <div class="caption" style="top:164px">I wish to improve my health situation</div>
  <svg class="abs" style="left:50px;top:190px" width="36" height="36" viewBox="0 0 24 24"><path d="M2 21h3V10H2zM22 11c0-1.1-.9-2-2-2h-6l1-4.6c0-.4-.2-.8-.4-1.1L13.7 2.5 8 8.2c-.3.3-.5.8-.5 1.3V19c0 1.1.9 2 2 2h8c.8 0 1.5-.5 1.8-1.2l2.6-6.2c.1-.2.1-.5.1-.7z" fill="none" stroke="var(--green-deep)" stroke-width="1.1" stroke-linejoin="round"/></svg>
  <svg class="abs" style="left:136px;top:194px" width="36" height="36" viewBox="0 0 24 24"><g transform="rotate(180 12 12)"><path d="M2 21h3V10H2zM22 11c0-1.1-.9-2-2-2h-6l1-4.6c0-.4-.2-.8-.4-1.1L13.7 2.5 8 8.2c-.3.3-.5.8-.5 1.3V19c0 1.1.9 2 2 2h8c.8 0 1.5-.5 1.8-1.2l2.6-6.2c.1-.2.1-.5.1-.7z" fill="none" stroke="var(--red)" stroke-width="1.1" stroke-linejoin="round"/></g></svg>
  <div class="textarea" style="top:248px;height:93px">Notes</div>
  <div class="btn btn-green" style="top:354px;width:94px"><svg width="11" height="7"><path d="M0.5 4.5L3 2L6 5L10.5 1" stroke="#fff" fill="none" stroke-width="1.1"/></svg>Statistics</div>
  <div class="btn btn-blue" style="top:354px;left:118px;width:94px">Gem</div>
</section>

<!-- Row 2 -->
<section class="screen" style="left:20px;top:510px">
  <div class="status"><svg width="7" height="7"><path d="M7 0V7H0Z" fill="#fff" opacity=".8"/></svg><svg width="5" height="7"><rect x="0.5" y="0.5" width="4" height="6" fill="#fff"/></svg>02:40</div>
  <header class="appbar"><svg class="back" width="7" height="11"><path d="M6 1L1.5 5.5L6 10" stroke="#fff" stroke-width="1.5" fill="none"/></svg>Statistics</header>
  <div class="dropband"></div>
  <div class="dropdown">Last Week<svg width="8" height="5"><path d="M1 1L4 4L7 1" stroke="#777" fill="none"/></svg></div>
  <div class="card">
    <div class="card-head">Week 14</div>
    <div class="day">Monday<span class="dot ok"></span></div>
    <div class="day">Tuesday<span class="dot bad"></span></div>
    <div class="day">Wednesday<span class="dot bad"></span></div>
    <div class="day">Thursday<span class="dot ok"></span></div>
    <div class="day">Friday<span class="dot ok"></span></div>
    <div class="day">Saturday<span class="dot ok"></span></div>
    <div class="day">Sunday<span class="dot ok"></span></div>
  </div>
</section>

<section class="screen" style="left:254px;top:510px">
  <div class="status"><svg width="7" height="7"><path d="M7 0V7H0Z" fill="#fff" opacity=".8"/></svg><svg width="5" height="7"><rect x="0.5" y="0.5" width="4" height="6" fill="#fff"/></svg>02:40</div>
  <header class="appbar"><svg class="back" width="7" height="11"><path d="M6 1L1.5 5.5L6 10" stroke="#fff" stroke-width="1.5" fill="none"/></svg>Statistics</header>
  <div class="dropband"></div>
  <div class="dropdown">Last Month<svg width="8" height="5"><path d="M1 1L4 4L7 1" stroke="#777" fill="none"/></svg></div>
  <div class="card">
    <div class="card-head"><span>Week 13</span><span>Week 14</span></div>
    <div class="calendar">
      <div class="wd">MON</div><div class="wd">TUE</div><div class="wd">WED</div><div class="wd">THU</div><div class="wd">FRI</div><div class="wd">SAT</div><div class="wd">SUN</div>
      <div class="cell"></div><div class="cell"></div><div class="cell"><span>1</span></div><div class="cell"><span>2</span></div><div class="cell"><span>3</span></div><div class="cell"><span>4</span></div><div class="cell"><span>5</span></div>
      <div class="cell"><span>6</span></div><div class="cell g"><span>7</span></div><div class="cell r"><span>8</span></div><div class="cell g"><span>9</span></div><div class="cell g"><span>10</span></div><div class="cell r"><span>11</span></div><div class="cell r"><span>12</span></div>
      <div class="cell g"><span>13</span></div><div class="cell g"><span>14</span></div><div class="cell r"><span>15</span></div><div class="cell"><span>16</span></div><div class="cell"><span>17</span></div><div class="cell"><span>18</span></div><div class="cell"><span>19</span></div>
      <div class="cell"><span>20</span></div><div class="cell"><span>21</span></div><div class="cell"><span>22</span></div><div class="cell"><span>23</span></div><div class="cell"><span>24</span></div><div class="cell"><span>25</span></div><div class="cell"><span>26</span></div>
      <div class="cell"><span>27</span></div><div class="cell"><span>28</span></div><div class="cell"><span>29</span></div><div class="cell"><span>30</span></div><div class="cell"></div><div class="cell"></div><div class="cell"></div>
    </div>
  </div>
  <div class="btn btn-grey" style="top:354px">Back</div>
</section>

<section class="screen" style="left:488px;top:510px">
  <div class="status"><svg width="7" height="7"><path d="M7 0V7H0Z" fill="#fff" opacity=".8"/></svg><svg width="5" height="7"><rect x="0.5" y="0.5" width="4" height="6" fill="#fff"/></svg>02:40</div>
  <header class="appbar">Send SMS to Consultant</header>
  <div class="abs" style="left:0;top:50px;width:225px;height:36px;background:var(--white);border-bottom:1px solid var(--line)"></div>
  <div class="caption" style="top:62px">Send SMS to one of your consultant</div>
  <div class="row" style="top:86px"><div class="avatar" role="img" aria-label="Portrait of consultant Milo Harrow"></div><span class="name">Milo Harrow</span><svg width="12" height="12" viewBox="0 0 24 24"><path d="M6.6 10.8c1.4 2.8 3.8 5.1 6.6 6.6l2.2-2.2c.3-.3.7-.4 1-.2 1.1.4 2.3.6 3.6.6.6 0 1 .4 1 1V20c0 .6-.4 1-1 1C10.6 21 3 13.4 3 4c0-.6.4-1 1-1h3.5c.6 0 1 .4 1 1 0 1.3.2 2.5.6 3.6.1.3 0 .7-.2 1z" fill="none" stroke="var(--green-deep)" stroke-width="1.6"/></svg></div>
  <div class="row" style="top:134px"><div class="avatar" role="img" aria-label="Portrait of consultant Dane Colby"></div><span class="name">Dane Colby</span><svg width="12" height="12" viewBox="0 0 24 24"><path d="M6.6 10.8c1.4 2.8 3.8 5.1 6.6 6.6l2.2-2.2c.3-.3.7-.4 1-.2 1.1.4 2.3.6 3.6.6.6 0 1 .4 1 1V20c0 .6-.4 1-1 1C10.6 21 3 13.4 3 4c0-.6.4-1 1-1h3.5c.6 0 1 .4 1 1 0 1.3.2 2.5.6 3.6.1.3 0 .7-.2 1z" fill="none" stroke="var(--green-deep)" stroke-width="1.6"/></svg></div>
  <div class="row" style="top:182px"><div class="avatar" role="img" aria-label="Portrait of consultant Ivo Brandt"></div><span class="name">Ivo Brandt</span><svg width="12" height="12" viewBox="0 0 24 24"><path d="M6.6 10.8c1.4 2.8 3.8 5.1 6.6 6.6l2.2-2.2c.3-.3.7-.4 1-.2 1.1.4 2.3.6 3.6.6.6 0 1 .4 1 1V20c0 .6-.4 1-1 1C10.6 21 3 13.4 3 4c0-.6.4-1 1-1h3.5c.6 0 1 .4 1 1 0 1.3.2 2.5.6 3.6.1.3 0 .7-.2 1z" fill="none" stroke="var(--green-deep)" stroke-width="1.6"/></svg></div>
  <div class="row" style="top:230px"><div class="avatar" role="img" aria-label="Portrait of consultant Teo Marsh"></div><span class="name">Teo Marsh</span><svg width="12" height="12" viewBox="0 0 24 24"><path d="M6.6 10.8c1.4 2.8 3.8 5.1 6.6 6.6l2.2-2.2c.3-.3.7-.4 1-.2 1.1.4 2.3.6 3.6.6.6 0 1 .4 1 1V20c0 .6-.4 1-1 1C10.6 21 3 13.4 3 4c0-.6.4-1 1-1h3.5c.6 0 1 .4 1 1 0 1.3.2 2.5.6 3.6.1.3 0 .7-.2 1z" fill="none" stroke="var(--green-deep)" stroke-width="1.6"/></svg></div>
  <div class="row" style="top:278px"><div class="avatar" role="img" aria-label="Portrait of consultant Gil Ashford"></div><span class="name">Gil Ashford</span><svg width="12" height="12" viewBox="0 0 24 24"><path d="M6.6 10.8c1.4 2.8 3.8 5.1 6.6 6.6l2.2-2.2c.3-.3.7-.4 1-.2 1.1.4 2.3.6 3.6.6.6 0 1 .4 1 1V20c0 .6-.4 1-1 1C10.6 21 3 13.4 3 4c0-.6.4-1 1-1h3.5c.6 0 1 .4 1 1 0 1.3.2 2.5.6 3.6.1.3 0 .7-.2 1z" fill="none" stroke="var(--green-deep)" stroke-width="1.6"/></svg></div>
</section>

<section class="screen" style="left:721px;top:510px">
  <div class="status"><svg width="7" height="7"><path d="M7 0V7H0Z" fill="#fff" opacity=".8"/></svg><svg width="5" height="7"><rect x="0.5" y="0.5" width="4" height="6" fill="#fff"/></svg>02:40</div>
  <header class="appbar">Send SMS to Consultant</header>
  <div class="abs" style="left:0;top:50px;width:225px;height:46px;background:var(--white)"></div>
  <div class="caption" style="top:62px">Please write the text for the SMS<br>&amp; confirm that you want to send it to</div>
  <div class="textarea" style="top:98px;height:202px">Please type your SMS here..</div>
  <div class="btn btn-blue" style="top:312px">Send</div>
  <div class="btn btn-grey" style="top:354px"><svg width="7" height="7"><path d="M1 1L6 6M6 1L1 6" stroke="#3d4247" stroke-width="1.2"/></svg>Cancel</div>
</section>

<section class="screen" style="left:955px;top:510px">
  <div class="status"><svg width="7" height="7"><path d="M7 0V7H0Z" fill="#fff" opacity=".8"/></svg><svg width="5" height="7"><rect x="0.5" y="0.5" width="4" height="6" fill="#fff"/></svg>02:40</div>
  <header class="appbar">SMS Confirmation</header>
  <span class="tick abs" style="left:38px;top:89px"><svg width="8" height="8"><path d="M1 4L3.2 6.2L7 2" stroke="#fff" stroke-width="1.3" fill="none"/></svg></span>
  <div class="abs" style="left:66px;top:87px;font-size:11px;line-height:12px;color:var(--muted)">Oren Vasko has now<br>recieved your SMS</div>
  <div class="btn btn-blue" style="top:150px">OK</div>
</section>

</body>
</html>
```